Web design for a crypto donation landing page for wildlife protection projects

We are developing the landing page for the presale of a web3 project, which will collect cryptos to send them to wildlife protection projects.
Here some website we like:
https://www.tidegroveaccord.fr/
https://qelvo.io/
https://www.mossvalen.io/
please, use the wireframe to know what blocks we want but we accept different template.
If possible, do the design on figma. Use 1 or 2 fonts max. Used green, blue and white, no more. Make a consistent system design by using the same font size for H1, H2, H3... and the same colors everywhere.

```html
<!DOCTYPE html>
<html lang="fr">
<head>
<meta charset="utf-8">
<title>Sevebrin — Protégeons la nature ensemble</title>
<link href="https://fonts.googleapis.com/css2?family=Lexend:wght@400;500;600&family=Poppins:wght@300;400;500;600&display=swap" rel="stylesheet">
<style>
:root{
  --purple:#2b1584;
  --purple-light:#3a22a0;
  --green:#6cc417;
  --green-dark:#1f5c2a;
  --black:#000;
  --white:#fff;
  --ink:#1b1b1b;
  --grey:#555;
  --line:#d9d9d9;
  --sea-1:#7fb5b0;
  --sea-2:#5d8f86;
  --forest:#15231f;
  --head:"Lexend",sans-serif;
  --body:"Poppins",sans-serif;
}
*{box-sizing:border-box;margin:0;padding:0}
html,body{width:1200px;height:4413px;overflow:hidden}
body{position:relative;font-family:var(--body);color:var(--ink);background:var(--white)}
.abs{position:absolute}
.h2{font-family:var(--head);font-weight:500;font-size:33px;letter-spacing:1px;line-height:1.25;color:var(--ink)}

/* hero */
.hero{left:0;top:0;width:1200px;height:780px;background:var(--black)}
.hero-wave{left:0;top:560px;width:1200px;height:260px}
.brand-tab{left:0;top:0;width:340px;height:86px}
.brand{display:flex;align-items:center;gap:8px;font-family:var(--head);font-weight:500;color:var(--white)}
.brand-dot{width:32px;height:32px;border-radius:50%;background:var(--green)}
.tiger{left:660px;top:60px;width:540px;height:560px;background:radial-gradient(ellipse at 60% 45%,#b86a24 0%,#6b3a12 45%,#000 80%)}
.hero-title{left:108px;top:222px;font-family:var(--head);font-weight:500;font-size:31px;letter-spacing:2.5px;color:var(--white)}
.hero-title span{color:var(--green)}
.hero-sub{left:108px;top:266px;font-size:16px;font-weight:500;color:var(--white)}
.hero-text{left:108px;top:338px;width:500px;font-size:17px;line-height:25px;color:var(--white)}
.partners{left:110px;top:496px;display:flex;gap:48px}
.partners i{display:block;width:95px;height:22px;border-radius:11px;background:#8a8a8a}
.token-card{left:108px;top:592px;width:984px;height:118px;background:var(--white);border-radius:16px;display:flex;align-items:center;padding:0 42px}
.token-title{font-family:var(--head);font-weight:500;font-size:28px;letter-spacing:1px;color:var(--green-dark);width:330px}
.qty{width:198px;height:42px;border:2px solid #999;border-radius:21px;display:flex;justify-content:space-around;align-items:center;font-family:var(--head);font-size:28px;color:var(--green-dark)}
.rate{margin-left:32px;font-size:13px;color:#777;width:140px}
.buy{width:198px;height:42px;border-radius:21px;background:linear-gradient(90deg,#8bd41c,#3fa337);color:var(--white);font-size:13px;font-weight:600;display:flex;align-items:center;justify-content:center}

/* how */
.sea{left:0;top:700px;width:1200px;height:820px;background:linear-gradient(180deg,#9cc8c3 0%,var(--sea-1) 40%,var(--sea-2) 100%)}
.how-title{left:0;top:838px;width:1200px;text-align:center}
.step{top:980px;width:300px;height:302px;background:var(--purple);border-radius:14px;padding:30px 24px;color:var(--white)}
.step svg{width:44px;height:44px}
.step h3{margin-top:18px;font-size:14px;font-weight:600;letter-spacing:.5px;line-height:22px}
.step p{margin-top:14px;font-size:13px;line-height:22px}

/* community */
.com-title{left:108px;top:1575px;width:700px}
.com-lead{left:108px;top:1678px;width:700px;font-size:16px;font-weight:500;line-height:26px;color:#333}
.socials{left:108px;top:1746px;display:flex;gap:30px;font-size:17px}
.socials span{display:flex;align-items:center;gap:14px}
.socials i{width:42px;height:42px;border-radius:50%;background:var(--black)}
.com-intro{left:108px;top:1823px;font-size:17px}
.perks{left:112px;top:1862px;list-style:none;width:620px}
.perks li{display:flex;gap:20px;font-size:17px;line-height:20px;margin-bottom:22px}
.perks svg{flex:none;width:24px;height:24px;margin-top:3px}
.duck{left:850px;top:1586px;width:440px;height:445px;border-radius:50%;background:radial-gradient(circle at 45% 55%,#8a6a4a 0%,#d9b89c 35%,#4a3a34 80%)}

/* roadmap */
.forest{left:0;top:2150px;width:1200px;height:540px;background:var(--forest)}
.roadmap{left:112px;top:2068px;width:978px;height:612px;background:linear-gradient(160deg,var(--purple) 0%,#33209a 100%);border-radius:16px;overflow:hidden;color:var(--white)}
.rm-title{position:absolute;left:0;top:44px;width:100%;text-align:center;font-family:var(--head);font-weight:500;font-size:32px;letter-spacing:3px}
.rm-arrows{position:absolute;left:450px;top:88px}
.rm-line{position:absolute;left:0;top:327px;width:100%;height:3px;background:var(--green)}
.dot{position:absolute;top:318px;width:22px;height:22px;border-radius:50%;background:var(--green)}
.stem{position:absolute;width:2px;background:var(--green)}
.quarter{position:absolute;font-family:var(--head);font-size:19px;letter-spacing:1px}
.tasks{position:absolute;list-style:none;font-size:12px;line-height:27px}
.tasks li::before{content:"• "}

/* faq */
.bird{left:0;top:2680px;width:1200px;height:420px;background:linear-gradient(180deg,#1c2a22 0%,#7a2a20 35%,#c9cfc9 75%,#fff 100%)}
.faq-title{left:0;top:3022px;width:1200px;text-align:center}
.faq{left:158px;top:3090px;width:884px;list-style:none}
.faq li{border-bottom:1px solid var(--line);padding:13px 16px;font-size:13px;font-weight:500;display:flex;flex-wrap:wrap;justify-content:space-between;align-items:center;height:47px}
.faq li.open{height:87px;align-items:flex-start}
.faq li p{width:100%;padding:8px 28px 0;font-size:11.5px;font-weight:400;line-height:24px;color:#444}

/* team */
.team-bg{left:0;top:3470px;width:1200px;height:560px;background:linear-gradient(180deg,#fff 0%,#eef3f7 100%)}
.team-title{left:0;top:3588px;width:1200px;text-align:center}
.member{top:3658px;width:190px}
.member .photo{width:190px;height:222px;background:linear-gradient(180deg,#f4f4f4,#d8dde4)}
.member h4{margin-top:12px;font-size:16px;font-weight:500;line-height:20px}
.member p{margin-top:12px;font-size:13px;color:#444;line-height:20px}

/* footer */
.footer-wave{left:0;top:3990px;width:1200px;height:423px}
.foot-brand{left:108px;top:4180px;font-size:26px}
.foot-brand .brand-dot{width:58px;height:58px}
.foot-info{left:370px;top:4186px;color:var(--white);font-size:16px;line-height:22px}
.foot-info p{margin-bottom:22px}
.contact-btn{left:864px;top:4195px;width:226px;height:42px;border:2px solid var(--white);border-radius:21px;color:var(--white);font-size:14px;font-weight:600;display:flex;align-items:center;justify-content:center;letter-spacing:.5px}
.foot-icons{left:924px;top:4312px;display:flex;gap:26px}
.foot-icons i{width:20px;height:20px;border-radius:50%;background:var(--white)}
.foot-url{left:0;top:4396px;width:1200px;text-align:center;font-size:13px;color:#8f86c2}
</style>
</head>
<body>

<!-- Hero -->
<section class="abs hero"></section>
<div class="abs tiger" role="img" aria-label="Portrait photographique d'un tigre sur fond noir"></div>
<svg class="abs hero-wave" viewBox="0 0 1200 260" preserveAspectRatio="none"><path d="M0 160 C220 80 420 150 640 150 C860 150 1000 240 1200 200 L1200 0 L0 0 Z" fill="#000"/></svg>
<svg class="abs brand-tab" viewBox="0 0 340 86"><path d="M0 0 H340 C320 60 290 86 240 86 H0 Z" fill="#2b1584"/></svg>
<div class="abs brand" style="left:108px;top:22px;font-size:17px"><span class="brand-dot" style="width:24px;height:24px"></span>Sevebrin</div>

<h1 class="abs hero-title">Protégeons la <span>nature</span> ensemble</h1>
<p class="abs hero-sub">Faites un don de tokens et aidez à protéger la faune et flore.</p>
<p class="abs hero-text">Notre plateforme vous permet d’ajouter des tokens dev otre choix pour les donner a un projet de protectiond e la nature. Votre contribution aidera à financer des actions concrètes pour préserver l’environnement.</p>
<div class="abs partners"><i></i><i></i><i></i></div>

<div class="abs token-card">
  <div class="token-title">ACHETER DES TOKEN</div>
  <div class="qty"><span>-</span><span>12</span><span>+</span></div>
  <div class="rate">12 token = €30</div>
  <div class="buy">ACHETER</div>
</div>

<!-- How it works -->
<div class="abs sea" role="img" aria-label="Photographie sous-marine d'une tortue de mer au-dessus d'un récif"></div>
<svg class="abs" style="left:0;top:680px" width="1200" height="120" viewBox="0 0 1200 120" preserveAspectRatio="none"><path d="M0 40 C220 0 420 60 640 60 C860 60 1000 110 1200 70 L1200 0 L0 0 Z" fill="#000"/></svg>
<h2 class="abs h2 how-title">Comment protéger la nature avec<br>des tokens Sevebrin?</h2>

<div class="abs step" style="left:110px">
  <svg viewBox="0 0 44 44" fill="none" stroke="#6cc417" stroke-width="2"><circle cx="22" cy="22" r="18"/><circle cx="22" cy="22" r="12"/><path d="M19 15v14M19 15h5a3 3 0 010 6h-5h6a3 3 0 010 7h-6"/></svg>
  <h3>ACHETEZ DES TOKENS<br>SEVEBRIN</h3>
  <p>Les tokens sont des actifs numériques qui peuvent être utilisés pour financer des projets des associations.</p>
</div>
<div class="abs step" style="left:450px">
  <svg viewBox="0 0 44 44" fill="none" stroke="#6cc417" stroke-width="2"><circle cx="22" cy="16" r="11"/><path d="M8 34c6-6 12-6 14-4h8M6 40l6-6M30 30c3-1 6-4 8-4"/></svg>
  <h3>VOTEZ POUR UN<br>PROJET</h3>
  <p>Vous pouvez voter pour un projet de votre choix. Les projets sont proposés par des associations et des ONG qui travaillent pour la</p>
</div>
<div class="abs step" style="left:792px">
  <svg viewBox="0 0 44 44" fill="none" stroke="#6cc417" stroke-width="2"><rect x="8" y="20" width="28" height="20"/><path d="M22 4v10M16 10l6-6 6 6M17 28c0-3 5-4 5 0 0-4 5-3 5 0s-5 6-5 6-5-3-5-6z"/></svg>
  <h3>L’ASSOCIATION CHOISIT<br>REÇOIT L’ARGENT</h3>
  <p>Le projet qui a reçu le plus de votes recevra les tokens. L’association pourra utiliser cet argent pour financer ses actions concrètes pour protéger la nature.</p>
</div>
<svg class="abs" style="left:0;top:1340px" width="1200" height="190" viewBox="0 0 1200 190" preserveAspectRatio="none"><path d="M0 150 C260 90 420 40 700 80 C900 110 1050 20 1200 10 L1200 190 L0 190 Z" fill="#fff"/></svg>

<!-- Community -->
<h2 class="abs h2 com-title">Rejoignez la communauté pour soutenir<br>la protection de la nature</h2>
<p class="abs com-lead">La nature est en danger, nous devons agir ensemble. Rejoignez la communaute pour soutenir la protection de la nature.</p>
<div class="abs socials"><span><i></i>Gathernest</span><span><i></i>Chirplane</span></div>
<p class="abs com-intro">En rejoignant la communaute, vous pourrez:</p>
<ul class="abs perks">
  <li><svg viewBox="0 0 24 24"><circle cx="12" cy="12" r="12" fill="#3fa337"/><path d="M7 12l3.5 3.5L17 9" stroke="#fff" stroke-width="2.4" fill="none"/></svg>Suivre les projets des associations qui travaillent pour la protection de la nature.</li>
  <li><svg viewBox="0 0 24 24"><circle cx="12" cy="12" r="12" fill="#3fa337"/><path d="M7 12l3.5 3.5L17 9" stroke="#fff" stroke-width="2.4" fill="none"/></svg>Voter pour le projet de votre choix et aider à financer ses actions concretes.</li>
  <li><svg viewBox="0 0 24 24"><circle cx="12" cy="12" r="12" fill="#3fa337"/><path d="M7 12l3.5 3.5L17 9" stroke="#fff" stroke-width="2.4" fill="none"/></svg>Etre informé des dernières actualités sur la protection de la nature.</li>
</ul>
<div class="abs duck" role="img" aria-label="Photographie de mains tenant délicatement un caneton"></div>

<!-- Roadmap -->
<div class="abs forest" role="img" aria-label="Fond photographique sombre de végétation"></div>
<section class="abs roadmap">
  <h2 class="rm-title">ROADMAP</h2>
  <svg class="rm-arrows" width="78" height="22" viewBox="0 0 78 22" fill="none" stroke="#fff" stroke-width="2"><path d="M2 11h28M10 3L2 11l8 8M48 11h28M68 3l8 8-8 8"/></svg>
  <div class="rm-line"></div>

  <div class="stem" style="left:104px;top:160px;height:170px"></div>
  <div class="dot" style="left:94px"></div>
  <ul class="tasks" style="left:118px;top:152px"><li>Site internet &amp; reseaux sociaux</li><li>Marketing &amp; development du smart contract tesnet</li><li>Juridique et Pre vente n'1</li><li>Developpment du smart contract tesnet</li></ul>
  <div class="quarter" style="left:92px;top:352px">Q1 2024</div>

  <div class="dot" style="left:364px"></div>
  <div class="stem" style="left:374px;top:330px;height:160px"></div>
  <div class="quarter" style="left:362px;top:280px">Q2 2024</div>
  <ul class="tasks" style="left:388px;top:414px"><li>Site internet &amp; reseaux sociaux</li><li>Marketing &amp; development du</li><li style="list-style:none">&nbsp;&nbsp;smart contract tesnet</li></ul>

  <div class="stem" style="left:634px;top:160px;height:170px"></div>
  <div class="dot" style="left:624px"></div>
  <ul class="tasks" style="left:648px;top:152px;white-space:nowrap"><li>Site internet &amp; reseaux sociaux</li><li>Marketing &amp; development du smart contract tesnet</li><li>Juridique et Pre vente n'1</li><li>Developpment du smart contract tesnet</li></ul>
  <div class="quarter" style="left:622px;top:352px">Q3 2024</div>

  <div class="dot" style="left:864px"></div>
  <div class="stem" style="left:874px;top:330px;height:140px"></div>
  <div class="quarter" style="left:864px;top:280px">Q4 2024</div>
  <ul class="tasks" style="left:888px;top:388px;white-space:nowrap"><li>Site internet &amp; reseaux</li><li>Marketing &amp; dev</li><li style="list-style:none">&nbsp;&nbsp;smart contract</li></ul>
</section>

<!-- FAQ -->
<div class="abs bird" role="img" aria-label="Photographie d'un oiseau rouge posé près de fleurs rouges"></div>
<h2 class="abs h2 faq-title">Frequently Asked Questions</h2>
<ul class="abs faq">
  <li class="open">Frequently Asked Question 1<svg width="16" height="10" viewBox="0 0 16 10"><path d="M2 8l6-6 6 6" stroke="#1f5c2a" stroke-width="2.4" fill="none"/></svg>
    <p>Lorem ipsum dolor sit amet, consectetur adipiscing elit, sed do eiusmod tempor incididunt ut labore et dolore magna aliqua. Quis ipsum suspendisse ultrices gravida maecenas, accumsan lacus vel facilisis.</p></li>
  <li>Frequently Asked Question 2<svg width="16" height="10" viewBox="0 0 16 10"><path d="M2 2l6 6 6-6" stroke="#1f5c2a" stroke-width="2.4" fill="none"/></svg></li>
  <li>Frequently Asked Question 3<svg width="16" height="10" viewBox="0 0 16 10"><path d="M2 2l6 6 6-6" stroke="#1f5c2a" stroke-width="2.4" fill="none"/></svg></li>
  <li>Frequently Asked Question 4<svg width="16" height="10" viewBox="0 0 16 10"><path d="M2 2l6 6 6-6" stroke="#1f5c2a" stroke-width="2.4" fill="none"/></svg></li>
  <li>Frequently Asked Question 5<svg width="16" height="10" viewBox="0 0 16 10"><path d="M2 2l6 6 6-6" stroke="#1f5c2a" stroke-width="2.4" fill="none"/></svg></li>
  <li>Frequently Asked Question 6<svg width="16" height="10" viewBox="0 0 16 10"><path d="M2 2l6 6 6-6" stroke="#1f5c2a" stroke-width="2.4" fill="none"/></svg></li>
</ul>

<!-- Team -->
<div class="abs team-bg"></div>
<h2 class="abs h2 team-title">Meet The Team</h2>
<div class="abs member" style="left:208px"><div class="photo" role="img" aria-label="Portrait du fondateur"></div><h4>Marchetti<br>Alban</h4><p>Fondateur</p></div>
<div class="abs member" style="left:505px"><div class="photo" role="img" aria-label="Portrait de la développeuse blockchain"></div><h4>Lestrade<br>Ines</h4><p>Developpeuse<br>blockchain</p></div>
<div class="abs member" style="left:803px"><div class="photo" role="img" aria-label="Portrait de la développeuse front-end"></div><h4>Durand<br>Salome</h4><p>Developpeur front-end</p></div>

<!-- Footer -->
<svg class="abs footer-wave" viewBox="0 0 1200 423" preserveAspectRatio="none"><path d="M0 60 C260 120 520 10 800 40 C980 60 1100 20 1200 0 L1200 423 L0 423 Z" fill="#2b1584"/></svg>
<div class="abs brand foot-brand" style="flex-direction:column;align-items:center;gap:10px"><span class="brand-dot"></span>Sevebrin</div>
<div class="abs foot-info">
  <p>14 Rue des Tilleuls<br>Paris 3C</p>
  <p>+33 000 482<br>hello@sevebrin.org</p>
  <p>Terms &amp; Conditions</p>
</div>
<div class="abs contact-btn">CONTACT US</div>
<div class="abs foot-icons"><i></i><i></i><i></i></div>
<div class="abs foot-url">www.sevebrin.org</div>

</body>
</html>
```